Radiant Harvest Gathering 2021

I am looking to create a flyer for a one day prayer retreat our church is organizing. This flyer will be posted on social media, websites, mobile apps, and will also be printed so it can be mailed to people.

I am looking for something professional, with good use of our logo and band colors (logo colors).

I am counting on the designer's skill, creativity, art and knowledge of media communication to produce a flyer that will effectively and quickly convey the message we are trying to spread.

CONTENT OF THE FLYER:
Event title: Radiant Harvest Gathering
Date: Tuesday July 2nd, 2021
Time: 11:00AM - 7:00PM
Bellmore Hotel, 4817 Wexley Avenue, Portland, Maine 04109 (Room: Tamarind)
Event Key words to highlight what the event is about: Prayer, Fasting, Worship, Prophecy, Revival.
Key phrases:
A one day prayer retreat.
Jesus Chris is Lord

Contact info:
www.quvello.org
Phone: 207 555 0148
Email: contact@brookmeadow.org

```html
<!DOCTYPE html>
<html lang="en">
<head>
<meta charset="utf-8">
<title>Radiant Harvest Gathering 2021</title>
<link rel="stylesheet" href="https://fonts.googleapis.com/css2?family=Kaushan+Script&family=Libre+Baskerville:wght@400;700&family=Open+Sans:wght@600;700;800&family=Orbitron:wght@800&display=swap">
<style>
  :root {
    --ice-light: #f3f5f9;
    --ice-mid: #dfe4ec;
    --ink-navy: #1f3350;
    --royal-blue: #2f3f96;
    --deep-purple: #35237f;
    --address-blue: #3b4aa2;
    --title-white: #f7f7fb;
    --title-edge: #4b2fa0;
    --flame-orange: #ee9322;
    --note-paper: #faf3d2;
    --tick-yellow: #f2b51c;
    --pill-blue: #8fd0f5;
    --footer-navy: #1e3552;
    --white: #ffffff;
  }
  html, body { margin: 0; padding: 0; overflow: hidden; }
  body { width: 816px; height: 1200px; background: var(--ice-light); }
  .flyer {
    position: relative; width: 816px; height: 1200px; overflow: hidden;
    font-family: "Open Sans", Arial, sans-serif;
  }
  .ice-backdrop {
    position: absolute; inset: 0 0 173px 0;
    background: radial-gradient(ellipse at 50% 40%, var(--ice-light) 0%, #eceff5 55%, var(--ice-mid) 100%);
  }
  .abs { position: absolute; margin: 0; }
  .tagline-lord {
    top: 44px; left: 0; width: 816px; text-align: center;
    font-family: "Kaushan Script", cursive; font-size: 36px; color: var(--ink-navy);
  }
  .vine-ornament {
    top: 104px; left: 314px; width: 224px; height: 14px; border-radius: 7px;
    background: linear-gradient(90deg, transparent, #9aa5b8 30%, #9aa5b8 70%, transparent);
    opacity: .6;
  }
  .event-title { top: 160px; left: 90px; width: 630px; height: 125px;
    filter: drop-shadow(2px 3px 0 var(--title-edge)) drop-shadow(0 4px 4px rgba(40,30,100,.35)); }
  .event-title text { font-family: "Orbitron", sans-serif; font-weight: 800; fill: var(--title-white); stroke: #c9cbd8; stroke-width: .8; }
  .retreat-line {
    top: 298px; left: 0; width: 816px; text-align: center;
    font-family: "Libre Baskerville", serif; font-size: 21px; letter-spacing: 9px;
    color: var(--ink-navy);
  }
  .bible-photo {
    top: 333px; left: 282px; width: 224px; height: 372px; border-radius: 10px;
    background: linear-gradient(180deg, rgba(70,70,75,.75) 0%, rgba(120,115,115,.45) 50%, rgba(220,205,200,.15) 100%);
    filter: blur(1px);
  }
  .date-day, .date-month {
    left: 96px; font-weight: 800; color: var(--royal-blue); letter-spacing: -3px; line-height: 1;
  }
  .date-day { top: 548px; font-size: 64px; }
  .date-month { top: 624px; font-size: 58px; }
  .date-month sup { font-size: 30px; vertical-align: 26px; letter-spacing: -1px; margin-left: 6px; }
  .year-bar {
    top: 556px; left: 383px; width: 50px; height: 131px; background: var(--flame-orange);
    display: flex; align-items: center; justify-content: center;
  }
  .year-bar span {
    transform: rotate(-90deg); color: var(--white); font-weight: 800; font-size: 34px; letter-spacing: -1px;
  }
  .event-time {
    top: 548px; left: 440px; font-size: 40px; font-weight: 800; letter-spacing: -2.5px; color: var(--deep-purple);
  }
  .venue {
    top: 618px; left: 447px; font-size: 15.5px; font-weight: 700; line-height: 24px;
    color: var(--address-blue); letter-spacing: -.2px;
  }
  .keyword-note {
    top: 736px; left: 314px; width: 166px; height: 245px;
    transform: rotate(-19deg); background: var(--note-paper);
    box-shadow: 4px 6px 12px rgba(0,0,0,.25);
  }
  .keyword-note ul { list-style: none; margin: 0; padding: 34px 0 0 18px; }
  .keyword-note li {
    font-family: "Kaushan Script", cursive; font-size: 28px; line-height: 39px; color: #1b1b22;
    display: flex; align-items: center; gap: 6px;
  }
  .keyword-note svg { width: 14px; height: 14px; flex: none; }
  .footer-band {
    left: 0; top: 1027px; width: 816px; height: 173px; background: var(--footer-navy);
  }
  .brand {
    top: 1062px; left: 128px; display: flex; align-items: center; gap: 10px;
    color: var(--white); font-size: 34px; font-weight: 600; letter-spacing: 1px;
  }
  .brand i { width: 14px; height: 14px; border-radius: 50%; background: var(--flame-orange); display: block; }
  .call-pill {
    top: 1064px; left: 360px; width: 104px; height: 28px; border-radius: 6px; background: var(--pill-blue);
    color: var(--footer-navy); font-weight: 800; font-size: 19px; text-align: center; line-height: 28px; letter-spacing: -.5px;
  }
  .phone {
    top: 1052px; left: 481px; color: var(--white); font-size: 38px; font-weight: 800; letter-spacing: .5px;
  }
  .contact-row {
    top: 1103px; left: 360px; display: flex; align-items: center; gap: 7px;
    color: var(--white); font-size: 16px; font-weight: 700;
  }
  .contact-row svg { width: 16px; height: 16px; }
</style>
</head>
<body>
<main class="flyer">
  <div class="ice-backdrop" role="img" aria-label="Soft frosted ice texture background"></div>

  <p class="abs tagline-lord">Jesus Christ is Lord</p>
  <div class="abs vine-ornament" role="img" aria-label="Small leafy vine ornament"></div>

  <svg class="abs event-title" viewBox="0 0 630 125" aria-label="Radiant Harvest Gathering">
    <text x="3" y="52" font-size="54" textLength="624" lengthAdjust="spacingAndGlyphs">RADIANT HARVEST</text>
    <text x="3" y="118" font-size="64" textLength="624" lengthAdjust="spacingAndGlyphs">GATHERING</text>
  </svg>

  <p class="abs retreat-line">A ONE DAY PRAYER RETREAT</p>

  <div class="abs bible-photo" role="img" aria-label="Hands lifting a Holy Bible, faded into the background"></div>

  <p class="abs date-day">TUESDAY</p>
  <p class="abs date-month">JULY&nbsp;&nbsp;2<sup>ND</sup></p>
  <div class="abs year-bar"><span>2021</span></div>

  <p class="abs event-time">11:00 AM - 7:00 PM</p>
  <p class="abs venue">BELLMORE HOTEL, 4817 WEXLEY AVENUE<br>PORTLAND, MAINE 04109<br>(ROOM: TAMARIND )</p>

  <div class="abs keyword-note" role="img" aria-label="Notepad with pencil listing the event keywords">
    <ul>
      <li><svg viewBox="0 0 14 14"><path d="M2 7l3 4 7-9" fill="none" stroke="var(--tick-yellow)" stroke-width="2.4"/></svg>Prayer</li>
      <li><svg viewBox="0 0 14 14"><path d="M2 7l3 4 7-9" fill="none" stroke="var(--tick-yellow)" stroke-width="2.4"/></svg>Fasting</li>
      <li><svg viewBox="0 0 14 14"><path d="M2 7l3 4 7-9" fill="none" stroke="var(--tick-yellow)" stroke-width="2.4"/></svg>Worship</li>
      <li><svg viewBox="0 0 14 14"><path d="M2 7l3 4 7-9" fill="none" stroke="var(--tick-yellow)" stroke-width="2.4"/></svg>Prophecy</li>
      <li><svg viewBox="0 0 14 14"><path d="M2 7l3 4 7-9" fill="none" stroke="var(--tick-yellow)" stroke-width="2.4"/></svg>Revival</li>
    </ul>
  </div>

  <footer class="abs footer-band"></footer>
  <div class="abs brand"><i></i>QUVELLO</div>
  <div class="abs call-pill">CALL US</div>
  <p class="abs phone">207 555 0148</p>
  <div class="abs contact-row">
    <svg viewBox="0 0 16 16"><rect x="1.5" y="3.5" width="13" height="9" fill="none" stroke="#fff" stroke-width="1.2"/><path d="M1.5 3.5l6.5 5 6.5-5" fill="none" stroke="#fff" stroke-width="1.2"/></svg>
    <span>contact@brookmeadow.org</span>
    <svg viewBox="0 0 16 16" style="margin-left:6px"><circle cx="8" cy="8" r="6.5" fill="none" stroke="#fff" stroke-width="1.1"/><ellipse cx="8" cy="8" rx="3" ry="6.5" fill="none" stroke="#fff" stroke-width="1.1"/><path d="M1.5 8h13M2.5 5h11M2.5 11h11" stroke="#fff" stroke-width="1"/></svg>
    <span>www.quvello.org</span>
  </div>
</main>
</body>
</html>
```